Business Card for Toffee Parlour

I have a logo for my candy buffet business, and need a business card designed using that logo. Toffee Parlour designs and builds beautiful and delicious candy and dessert tables for all kinds of events. The card should be simple, modern, graphic, colorful, and use the Toffee Parlour Logo.

Target Market(s)

The target market is people hosting major parties and events. This includes brides getting married, parents hosting birthday parties/Sweet Sixteen/Bar Mitzvah/quinceanera parties, and companies hosting corporate events.

Industry/Entity Type

Business

Requirements
Must have
• The business card must have the logo, with or without the tag line.

The following information must be on the card:

Renata Hollis
CEO & Candy Stylist
415.372.6091
renata@toffeeparlourco.example
Nice to have
• I like the idea of having multiple colors of the same design so that several people receiving cards will each receive a different color. Perhaps 3-5 colors or variations on a basic card design.

```html
<!DOCTYPE html>
<html lang="en">
<head>
<meta charset="utf-8">
<title>Toffee Parlour – Business Card Colour Set</title>
<link rel="stylesheet" href="https://fonts.googleapis.com/css2?family=Arvo:wght@400;700&display=swap">
<style>
  :root {
    --sheet: #ffffff;
    --frame: #3b7fc2;
    --logo-ink: #1a1a1a;
    --marker: #e8564c;
    --blue: #1b9ad6;   --blue-tint: #e0ecf7;
    --pink: #e6197d;   --pink-tint: #f9dbe8;
    --orange: #f7a047; --orange-tint: #fde9d6;
    --green: #1a9450;  --green-tint: #dde9dc;
    --purple: #6a5fa5; --purple-tint: #dcd8ea; --purple-mid: #b9b2d8;
  }
  * { margin: 0; padding: 0; box-sizing: border-box; }
  html, body { width: 1200px; height: 675px; overflow: hidden; background: var(--sheet); }
  body { position: relative; font-family: "Arvo", serif; }

  .card {
    position: absolute; width: 218px; height: 141px;
    border: 1px solid var(--frame); background: #fff; overflow: hidden;
    color: var(--ink);
  }
  .col-1 { left: 7px; }   .col-2 { left: 249px; } .col-3 { left: 490px; }
  .col-4 { left: 731px; } .col-5 { left: 973px; }
  .row-1 { top: 9px; }    .row-2 { top: 173px; }  .row-3 { top: 346px; } .row-4 { top: 526px; }

  .c-blue   { --ink: var(--blue);   --tint: var(--blue-tint); }
  .c-pink   { --ink: var(--pink);   --tint: var(--pink-tint); }
  .c-orange { --ink: var(--orange); --tint: var(--orange-tint); }
  .c-green  { --ink: var(--green);  --tint: var(--green-tint); }
  .c-purple { --ink: var(--purple); --tint: var(--purple-tint); }

  /* Front: wordmark */
  .brand {
    position: absolute; inset: 0; display: flex; align-items: center; justify-content: center; gap: 8px;
  }
  .brand-dot { width: 14px; height: 14px; border-radius: 50%; background: var(--logo-ink); }
  .brand-name { font-size: 19px; font-weight: 400; color: var(--logo-ink); letter-spacing: 0.2px; }

  /* Back: decoration + details */
  .decor { position: absolute; inset: 0; width: 100%; height: 100%; }
  .decor circle { fill: var(--tint); }
  .decor .mid { fill: var(--purple-mid); }

  .details {
    position: absolute; left: 10px; right: 0; top: 40px;
    text-align: center; font-weight: 700; font-size: 7.6px; line-height: 12.5px;
  }
  .name { font-size: 13.5px; line-height: 20px; }
  .name .last { font-weight: 400; }
  .ruled .details { left: 4px; right: 2px; top: 42px; }
  .ruled .name { display: flex; align-items: center; gap: 6px; font-size: 10.5px; line-height: 16px; }
  .ruled .name::before, .ruled .name::after { content: ""; flex: 1; height: 1px; background: var(--ink); }
  .ruled .details p:not(.name) { padding-left: 6px; }

  .marker {
    position: absolute; left: 199px; top: 80px; width: 10px; height: 10px;
    border: 1px solid var(--marker);
  }
  .marker::before, .marker::after { content: ""; position: absolute; background: var(--marker); }
  .marker::before { left: 1px; right: 1px; top: 3.5px; height: 1px; }
  .marker::after { top: 1px; bottom: 1px; left: 3.5px; width: 1px; }
</style>
</head>
<body>

<!-- Fronts -->
<section class="card row-1 col-1"><div class="brand"><span class="brand-dot"></span><span class="brand-name">Toffee Parlour</span></div></section>
<section class="card row-1 col-2"><div class="brand"><span class="brand-dot"></span><span class="brand-name">Toffee Parlour</span></div></section>
<section class="card row-1 col-3"><div class="brand"><span class="brand-dot"></span><span class="brand-name">Toffee Parlour</span></div></section>
<section class="card row-1 col-4"><div class="brand"><span class="brand-dot"></span><span class="brand-name">Toffee Parlour</span></div></section>
<section class="card row-1 col-5"><div class="brand"><span class="brand-dot"></span><span class="brand-name">Toffee Parlour</span></div></section>

<!-- Backs: large corner circle -->
<section class="card row-2 col-1 c-blue">
  <svg class="decor" viewBox="0 0 218 141"><circle cx="198" cy="95" r="88"/></svg>
  <div class="details"><p class="name">Renata <span class="last">Hollis</span></p><p>CEO &amp; Candy Stylist</p><p>415.372.6091</p><p>renata@toffeeparlourco.example</p></div>
  <span class="marker"></span>
</section>
<section class="card row-2 col-2 c-pink">
  <svg class="decor" viewBox="0 0 218 141"><circle cx="198" cy="95" r="88"/></svg>
  <div class="details"><p class="name">Renata <span class="last">Hollis</span></p><p>CEO &amp; Candy Stylist</p><p>415.372.6091</p><p>renata@toffeeparlourco.example</p></div>
  <span class="marker"></span>
</section>
<section class="card row-2 col-3 c-orange">
  <svg class="decor" viewBox="0 0 218 141"><circle cx="198" cy="95" r="88"/></svg>
  <div class="details"><p class="name">Renata <span class="last">Hollis</span></p><p>CEO &amp; Candy Stylist</p><p>415.372.6091</p><p>renata@toffeeparlourco.example</p></div>
  <span class="marker"></span>
</section>
<section class="card row-2 col-4 c-green">
  <svg class="decor" viewBox="0 0 218 141"><circle cx="198" cy="95" r="88"/></svg>
  <div class="details"><p class="name">Renata <span class="last">Hollis</span></p><p>CEO &amp; Candy Stylist</p><p>415.372.6091</p><p>renata@toffeeparlourco.example</p></div>
  <span class="marker"></span>
</section>
<section class="card row-2 col-5 c-purple">
  <svg class="decor" viewBox="0 0 218 141"><circle cx="198" cy="95" r="88"/></svg>
  <div class="details"><p class="name">Renata <span class="last">Hollis</span></p><p>CEO &amp; Candy Stylist</p><p>415.372.6091</p><p>renata@toffeeparlourco.example</p></div>
  <span class="marker"></span>
</section>

<!-- Backs: ruled name with corner circle -->
<section class="card ruled row-3 col-1 c-blue">
  <svg class="decor" viewBox="0 0 218 141"><circle cx="198" cy="95" r="88"/></svg>
  <div class="details"><p class="name"><span>Renata <span class="last">Hollis</span></span></p><p>CEO &amp; Candy Stylist</p><p>415.372.6091</p><p>renata@toffeeparlourco.example</p></div>
  <span class="marker"></span>
</section>
<section class="card ruled row-3 col-2 c-pink">
  <svg class="decor" viewBox="0 0 218 141"><circle cx="198" cy="95" r="88"/></svg>
  <div class="details"><p class="name"><span>Renata <span class="last">Hollis</span></span></p><p>CEO &amp; Candy Stylist</p><p>415.372.6091</p><p>renata@toffeeparlourco.example</p></div>
  <span class="marker"></span>
</section>
<section class="card ruled row-3 col-3 c-orange">
  <svg class="decor" viewBox="0 0 218 141"><circle cx="198" cy="95" r="88"/></svg>
  <div class="details"><p class="name"><span>Renata <span class="last">Hollis</span></span></p><p>CEO &amp; Candy Stylist</p><p>415.372.6091</p><p>renata@toffeeparlourco.example</p></div>
  <span class="marker"></span>
</section>
<section class="card ruled row-3 col-4 c-green">
  <svg class="decor" viewBox="0 0 218 141"><circle cx="198" cy="95" r="88"/></svg>
  <div class="details"><p class="name"><span>Renata <span class="last">Hollis</span></span></p><p>CEO &amp; Candy Stylist</p><p>415.372.6091</p><p>renata@toffeeparlourco.example</p></div>
  <span class="marker"></span>
</section>
<section class="card ruled row-3 col-5 c-purple">
  <svg class="decor" viewBox="0 0 218 141"><circle cx="198" cy="95" r="88"/></svg>
  <div class="details"><p class="name"><span>Renata <span class="last">Hollis</span></span></p><p>CEO &amp; Candy Stylist</p><p>415.372.6091</p><p>renata@toffeeparlourco.example</p></div>
  <span class="marker"></span>
</section>

<!-- Backs: ruled name with scattered circles -->
<section class="card ruled row-4 col-1 c-blue">
  <svg class="decor" viewBox="0 0 218 141"><circle cx="104" cy="143" r="88"/></svg>
  <div class="details"><p class="name"><span>Renata <span class="last">Hollis</span></span></p><p>CEO &amp; Candy Stylist</p><p>415.372.6091</p><p>renata@toffeeparlourco.example</p></div>
  <span class="marker"></span>
</section>
<section class="card ruled row-4 col-2 c-pink">
  <svg class="decor" viewBox="0 0 218 141"><circle cx="8" cy="12" r="13"/><circle cx="212" cy="131" r="13"/></svg>
  <div class="details"><p class="name"><span>Renata <span class="last">Hollis</span></span></p><p>CEO &amp; Candy Stylist</p><p>415.372.6091</p><p>renata@toffeeparlourco.example</p></div>
  <span class="marker"></span>
</section>
<section class="card ruled row-4 col-3 c-orange">
  <svg class="decor" viewBox="0 0 218 141"><circle cx="8" cy="10" r="14"/><circle cx="212" cy="10" r="14"/><circle cx="8" cy="131" r="14"/><circle cx="212" cy="131" r="14"/></svg>
  <div class="details"><p class="name"><span>Renata <span class="last">Hollis</span></span></p><p>CEO &amp; Candy Stylist</p><p>415.372.6091</p><p>renata@toffeeparlourco.example</p></div>
  <span class="marker"></span>
</section>
<section class="card ruled row-4 col-4 c-green">
  <svg class="decor" viewBox="0 0 218 141"><circle cx="24" cy="121" r="16"/><circle cx="53" cy="120" r="10"/><circle cx="47" cy="103" r="6"/></svg>
  <div class="details"><p class="name"><span>Renata <span class="last">Hollis</span></span></p><p>CEO &amp; Candy Stylist</p><p>415.372.6091</p><p>renata@toffeeparlourco.example</p></div>
  <span class="marker"></span>
</section>
<section class="card ruled row-4 col-5 c-purple">
  <svg class="decor" viewBox="0 0 218 141"><circle cx="22" cy="70" r="17"/><circle cx="187" cy="70" r="17"/><circle class="mid" cx="109" cy="69" r="31"/></svg>
  <div class="details"><p class="name"><span>Renata <span class="last">Hollis</span></span></p><p>CEO &amp; Candy Stylist</p><p>415.372.6091</p><p>renata@toffeeparlourco.example</p></div>
  <span class="marker"></span>
</section>

</body>
</html>
```